Parallel Ledger Geek needs a Business Card

A design that can be uploaded to us.plimbo.example to be used on their Velra paper stock. Full bleed 88mm x 59mm. For best results, use vector-based PDF. Pre-flight your PDFs using the 'Adobe PDF/X-1a' pre-set. They use the Coated GRACoL 2006 public ICC profile.

Solid Black Card (front and back). There will be a red edge all the way around the card. Centered from top to bottom aligned left (Corwen Halby), where the Cor is white in color with a red dot over the i, and the rest 'wen Halby' is faded black with a red dot over the i in Halby. This should dominate the card so choose an appropriate font size (we can adjust after the 1st draft). Bottom right will have 2 items in white 1)profile.example/chalby7 2)555.304.2287...these should be stacked and aligned right at the bottom. Card orientation is horizontal.

On the back in faded black text is the following quote
"You can never change things by fighting the existing reality. To change something build a new model, that makes the existing model obsolete." Ellsworth Prandle

I will defer to the designer on the font choices for the first draft.

Requirements
Must have
• examples of name design below in attached image. I also attached a card with the red edge for your review...the designer does not need to design the red edge, it is included in the description for your visualization when designing the card.

```html
<!DOCTYPE html>
<html lang="en">
<head>
<meta charset="utf-8">
<title>Corwen Halby – Business Card</title>
<link href="https://fonts.googleapis.com/css2?family=Lato:ital,wght@0,300;0,400;0,700;1,400&family=Felipa&display=swap" rel="stylesheet">
<style>
  :root {
    --card-black: #000000;
    --gap-white: #ffffff;
    --ink-white: #ffffff;
    --ink-fade-start: #8a8a8a;
    --ink-fade-end: #3a3a3a;
    --quote-grey: #8c8c8c;
    --edge-red: #e0141e;
    --edge-glow: rgba(255, 40, 40, 0.55);
  }
  * { margin: 0; padding: 0; box-sizing: border-box; }
  html, body {
    width: 1200px;
    height: 394px;
    overflow: hidden;
    background: var(--gap-white);
  }
  .sheet {
    position: relative;
    width: 1200px;
    height: 394px;
    background: var(--gap-white);
  }
  .card {
    position: absolute;
    top: 0;
    height: 394px;
    background: var(--card-black);
    overflow: hidden;
    font-family: "Lato", Arial, sans-serif;
  }
  .card--front { left: 0; width: 588px; }
  .card--back { left: 606px; width: 594px; }

  .edge-line {
    position: absolute;
    left: 0;
    right: 0;
    top: 274px;
    height: 4px;
    background: linear-gradient(to bottom, rgba(255,255,255,0) 0%, var(--edge-red) 35%, #ff6a6a 50%, var(--edge-red) 65%, rgba(255,255,255,0) 100%);
    box-shadow: 0 0 4px var(--edge-glow);
  }

  .name {
    position: absolute;
    left: 26px;
    top: 112px;
    font-weight: 700;
    font-size: 82px;
    line-height: 1;
    letter-spacing: -0.5px;
    white-space: nowrap;
  }
  .name__lead { color: var(--ink-white); }
  .name__rest {
    background: linear-gradient(to right, var(--ink-fade-start), var(--ink-fade-end));
    -webkit-background-clip: text;
    background-clip: text;
    color: transparent;
  }

  .contact {
    position: absolute;
    right: 32px;
    top: 302px;
    text-align: right;
    color: var(--ink-white);
    font-size: 24px;
    line-height: 36px;
    font-weight: 400;
  }

  .quote {
    position: absolute;
    left: 30px;
    right: 30px;
    top: 106px;
    text-align: center;
    color: var(--quote-grey);
    font-weight: 300;
    font-size: 19px;
    line-height: 30px;
  }
  .quote__author {
    position: absolute;
    right: 32px;
    top: 222px;
    font-family: "Felipa", "Times New Roman", serif;
    font-size: 25px;
    color: var(--ink-white);
    white-space: nowrap;
  }
</style>
</head>
<body>
  <div class="sheet">
    <section class="card card--front" aria-label="Card front">
      <h1 class="name"><span class="name__lead">Cor</span><span class="name__rest">wen Halby</span></h1>
      <div class="edge-line"></div>
      <div class="contact">
        <p class="contact__web">profile.example/chalby7</p>
        <p class="contact__phone">555.304.2287</p>
      </div>
    </section>

    <section class="card card--back" aria-label="Card back">
      <p class="quote">"You can never change things by fighting the existing reality. To change something build a new model, that makes the existing model obsolete."</p>
      <p class="quote__author">Ellsworth Prandle</p>
      <div class="edge-line"></div>
    </section>
  </div>
</body>
</html>
```